Boutique PEO needs a catchy snail mail and email marketing flyer

Our company provides services to our clients and co-employees throughout the entire life cycle of an employee's employment. It is very serious business to our clients' but we need a catchy message and look to attract the attention of prospective clients. I have attached some of the ideas we tried.

Target Market(s)

small to medium size companies

Font styles to use
Serif

Colors

Designer to choose colors to be used in the design.

```html
<!DOCTYPE html>
<html lang="en">
<head>
<meta charset="utf-8">
<title>HR Headaches Flyer</title>
<link href="https://fonts.googleapis.com/css2?family=League+Spartan:wght@700;800&family=Oswald:wght@300;400;700&family=Montserrat:wght@400&display=swap" rel="stylesheet">
<style>
  :root {
    --backdrop: #4a474b;
    --paper: #ffffff;
    --ink: #1c1c1c;
    --accent: #d4121a;
    --rule: #8a8a8a;
    --frame: #3a3a3a;
  }
  html, body {
    margin: 0;
    padding: 0;
    width: 1200px;
    height: 1200px;
    overflow: hidden;
    background: var(--backdrop);
  }
  .canvas {
    position: relative;
    width: 1200px;
    height: 1200px;
  }
  .card {
    position: absolute;
    left: 257px;
    width: 687px;
    height: 485px;
    display: block;
    box-shadow: 0 6px 18px rgba(0,0,0,0.35);
  }
  .card--front { top: 90px; }
  .card--back { top: 624px; }
  .headline-hr { font-family: "League Spartan", sans-serif; font-weight: 800; fill: var(--ink); }
  .headline-red { font-family: "Oswald", sans-serif; font-weight: 700; fill: var(--accent); }
  .headline-light { font-family: "Oswald", sans-serif; font-weight: 300; fill: var(--ink); }
  .headline-bold { font-family: "Oswald", sans-serif; font-weight: 700; fill: var(--ink); }
  .pitch-wide { font-family: "Montserrat", sans-serif; font-weight: 400; fill: var(--ink); }
  .pitch-accent { fill: var(--accent); }
  .pitch-strong { font-family: "League Spartan", sans-serif; font-weight: 700; fill: var(--ink); }
  .tagline-light { font-family: "Oswald", sans-serif; font-weight: 300; fill: var(--ink); }
  .tagline-strong { font-family: "Oswald", sans-serif; font-weight: 700; fill: var(--accent); }
</style>
</head>
<body>
<main class="canvas">

  <svg class="card card--front" viewBox="0 0 687 485" xmlns="http://www.w3.org/2000/svg">
    <defs>
      <linearGradient id="doghouseTone" x1="0" y1="0" x2="1" y2="1">
        <stop offset="0" stop-color="#2e2e2e"/>
        <stop offset="0.5" stop-color="#5a5652"/>
        <stop offset="1" stop-color="#2a2a2a"/>
      </linearGradient>
    </defs>
    <rect class="card-paper" width="687" height="485" fill="var(--paper)"/>
    <rect class="card-frame" x="6.5" y="6.5" width="674" height="472" fill="none" stroke="var(--frame)" stroke-width="1"/>
    <rect class="card-photo" x="326" y="0" width="361" height="485" fill="url(#doghouseTone)" role="img" aria-label="Photo of a sad pug sitting in the doorway of a weathered wooden doghouse"/>
    <text class="headline-hr" x="39" y="223" font-size="210" textLength="256" lengthAdjust="spacingAndGlyphs">HR</text>
    <text class="headline-red" x="39" y="287" font-size="66" textLength="259" lengthAdjust="spacingAndGlyphs">HEADACHES</text>
    <text class="headline-light" x="38" y="342" font-size="54" textLength="254" lengthAdjust="spacingAndGlyphs">have you in the</text>
    <text class="headline-bold" x="38" y="406" font-size="60" textLength="254" lengthAdjust="spacingAndGlyphs">DOGHOUSE?</text>
  </svg>

  <svg class="card card--back" viewBox="0 0 687 485" xmlns="http://www.w3.org/2000/svg">
    <defs>
      <linearGradient id="officeTone" x1="0" y1="0" x2="0" y2="1">
        <stop offset="0" stop-color="#dcdcdc"/>
        <stop offset="0.55" stop-color="#8e8e8e"/>
        <stop offset="1" stop-color="#5c5c5c"/>
      </linearGradient>
    </defs>
    <rect class="card-paper" width="687" height="485" fill="var(--paper)"/>
    <rect class="card-photo" x="0" y="0" width="687" height="242" fill="url(#officeTone)" role="img" aria-label="Photo of a busy open-plan office with a team working at desks"/>
    <rect class="card-frame" x="7.5" y="7.5" width="672" height="470" fill="none" stroke="var(--frame)" stroke-width="1"/>
    <text class="pitch-wide" x="87" y="306" font-size="31" textLength="514" lengthAdjust="spacingAndGlyphs"><tspan class="pitch-accent">HAND OFF THE HEADACHES</tspan> of</text>
    <text class="pitch-wide" x="87" y="344" font-size="31" textLength="514" lengthAdjust="spacingAndGlyphs">PAYROLL,HR &amp; COMPLIANCE TO</text>
    <text class="pitch-strong" x="87" y="378" font-size="32" textLength="510" lengthAdjust="spacingAndGlyphs">TALLOWAYSOLUTIONS AND FOCUS ON</text>
    <line class="pitch-rule" x1="87" y1="388" x2="601" y2="388" stroke="var(--rule)" stroke-width="1.5"/>
    <text x="87" y="436" font-size="52" textLength="512" lengthAdjust="spacingAndGlyphs"><tspan class="tagline-light">THE BUSINESS of </tspan><tspan class="tagline-strong">YOUR BUSINESS</tspan></text>
  </svg>

</main>
</body>
</html>
```